Real Estate Search Site Re-Design of 2 Pages

Looking for designs to optimize 2 pages of our current site design. Our site allows users to find properties to purchase or rent.

Basically there are 4 panes
1. The top red one where you actually type in what you''re looking for.
2. The map pane that shows the properties
3. The scrollable results pane.
4. Property details pane.

A typical search would go like this:
1. User fills in their search criteria in the top pane in red. Clicks Find Homes
2. Site updates the map with properties plotted that fit the criteria. Site also populates the results pane at the bottom. Site shows the most newest property that fits the search criteria on the right.
3. User will scroll through the results pane or the map and click a property.
4. Site will update the property details pane with information on the selected property.

Search/Results Page
This main page needs a search form area, a results area, an area to display details of a property selected, a map to show results, and an area to display a real estate agent's information. The design must be full-screen to use all the space on the screen. All information should fit on a 1366x768 screen size. Please see sample screen shot.

Property Details Page
This one can be fixed width of 978px. This page needs all the elements that are displayed in the sample PNG file. Ideally, we want to be able to see all important information without scrolling on a 1366x768 screen. The important information in this size are Pictures with controls, address, bedrooms, bathrooms, square feet, square feet of the lot, days on market, agent information, and buttons to request a showing or get more information.

Our Goal:
Our goal is to get create a different way to display the data in an effective way. We want different ways to show the search results, maybe a vertical, scrolling list of property information with pictures. Or even a horizontal scrolling results pane. It must contain:

1. A map of the results
2. A way to scroll through the search results (like we have currently in case someone wants to search/sort bedrooms or square footage)
3. A way to view details of the property
4. A way to display agent information/picture
Updates

There's a lot of good design work coming through. Thank you.

Perhaps review some other real estate sales sites for ideas on pane configuration. Example site links:
http://www.brovat.example/homes/for_sale/?gclid=QXmP7k2-tb9DHR4W1KzeqN5BCE (brovat.example)
http://www.pemnox.example/?sem=3.4.2.6.8.2.1.15&gclid=RJwz82m-tb9DHWcn4KzeuTpBHS (Pemnox.example)
http://www.quindert.example/map_search/results/i/ (quindert.example)

Our goal for the redesign is to display the data in a more effective way. Either with a better flow, more pictures, more information, smoother search process. Please see the updated brief for details. The main idea is to show the data in the most effective way possible.

Project Deadline Extended
Reason: Still looking at different ideas for the search results. We are still open for fresh ideas.

Industry/Entity Type

Real Estate

Font styles to use
Sans Serif

Colors
eb1f27

```html
<!DOCTYPE html>
<html lang="en">
<head>
<meta charset="utf-8">
<title>Home Search</title>
<link href="https://fonts.googleapis.com/css2?family=Roboto:wght@400;500;700&display=swap" rel="stylesheet">
<style>
:root{
  --brand:#eb1f27;
  --brand-dark:#c9141b;
  --orange:#f47a20;
  --ink:#333;
  --muted:#555;
  --band:#a3a3a3;
  --row-alt:#f2f2f2;
  --panel:#f2f2f2;
  --map:#ececec;
  --white:#fff;
}
*{box-sizing:border-box;margin:0;padding:0}
html,body{width:1200px;height:752px;overflow:hidden;background:var(--white);font-family:"Roboto",Arial,sans-serif;color:var(--ink)}
.page{position:relative;width:1200px;height:752px}
.search-bar{position:absolute;left:0;top:0;width:1185px;height:102px;background:var(--brand);color:var(--white)}
.brand{position:absolute;left:19px;top:32px;font-size:29px;font-weight:700}
.label{position:absolute;font-size:16px}
.field{position:absolute;height:35px;background:var(--white);color:#999;font-size:14px;padding:0 8px;line-height:35px;border-radius:1px}
.field .caret{position:absolute;right:10px;top:14px;width:0;height:0;border-left:6px solid transparent;border-right:6px solid transparent;border-top:7px solid #888}
.find-btn{position:absolute;left:378px;top:10px;width:150px;height:34px;background:var(--orange);border:1px solid #e06010;border-radius:2px;color:var(--white);font-size:16px;font-weight:500;line-height:32px;padding-left:42px}
.find-btn svg{position:absolute;left:13px;top:8px}
.lang{position:absolute;right:21px;top:10px;font-size:14px}
.lang span{color:#f6a5a8}
.lang .sep{margin:0 9px;color:#f6a5a8}
.nav{position:absolute;top:64px;font-size:16px}
.map{position:absolute;left:0;top:102px;width:885px;height:411px;background:linear-gradient(135deg,#efefef,#e4e4e4 60%,#ebebeb)}
.map .pin{position:absolute}
.results{position:absolute;left:0;top:513px;width:885px;height:239px}
.results-head{height:32px;background:var(--band);color:var(--white);font-size:14px;position:relative}
.results-head span,.row span{position:absolute}
.results-head span{top:9px}
.results-head span::after{content:"";display:inline-block;margin-left:5px;border-left:5px solid transparent;border-right:5px solid transparent;border-top:6px solid var(--white);vertical-align:2px}
.row{position:relative;height:26px;font-size:14px;width:870px}
.row:nth-child(even){background:var(--row-alt)}
.row span{top:5px}
.c1{left:16px}.c2{left:220px}.c3{left:375px}.c4{left:487px}.c5{left:558px}.c6{left:638px}.c7{left:725px}.c8{left:819px}
.results-head .c1{left:20px}.results-head .c3{left:378px}.results-head .c4{left:485px}
.table-scroll{position:absolute;right:0;top:32px;width:15px;height:207px;background:#f7f7f7;border-left:1px solid #e2e2e2}
.table-scroll .thumb{position:absolute;left:2px;top:18px;width:11px;height:42px;background:#ddd;border:1px solid #bbb;border-radius:2px}
.details{position:absolute;left:885px;top:102px;width:300px;height:650px}
.address{position:absolute;left:13px;top:11px;font-size:18px;line-height:22px;color:#222}
.photo{position:absolute;left:13px;top:57px;width:275px;height:183px;background:linear-gradient(180deg,#6c9cc4 0%,#8bb0cf 45%,#6b6a5e 62%,#7a6a52 100%)}
.photo .count{position:absolute;left:0;right:0;bottom:8px;text-align:center;color:var(--white);font-size:14px}
.photo svg{position:absolute;top:160px}
.price{position:absolute;left:13px;top:251px;font-size:16px;font-weight:700;color:var(--brand)}
.specs{position:absolute;left:13px;top:274px;font-size:14px;display:flex;gap:6px;align-items:center}
.specs svg{margin-right:2px}
.facts{position:absolute;left:13px;top:302px;font-size:14px;line-height:17.5px;color:#222}
.btn{position:absolute;top:397px;height:36px;background:var(--brand);color:var(--white);font-size:16px;font-weight:500;text-align:center;line-height:36px;border-radius:2px;border-bottom:2px solid var(--brand-dark)}
.courtesy{position:absolute;left:13px;top:445px;font-size:14px}
.agent{position:absolute;left:0;top:481px;width:300px;height:169px;background:var(--panel)}
.agent-photo{position:absolute;left:15px;top:15px;width:110px;height:121px;background:linear-gradient(180deg,#5a5048,#8a6e5c 55%,#b03036)}
.agent-info{position:absolute;left:136px;top:13px;font-size:14px;line-height:17.5px;color:#222}
.agent-info b{font-weight:700}
.page-scroll{position:absolute;left:1185px;top:0;width:15px;height:752px;background:#f0f0f0;border-left:1px solid #ddd}
.page-scroll .thumb{position:absolute;left:2px;top:18px;width:11px;height:46px;background:#dcdcdc;border:1px solid #bbb;border-radius:2px}
</style>
</head>
<body>
<div class="page">
  <header class="search-bar">
    <div class="brand">Logo</div>
    <div class="label" style="left:112px;top:19px">Location:</div>
    <div class="field" style="left:195px;top:10px;width:173px">Alhambra</div>
    <div class="find-btn"><svg width="18" height="18" viewBox="0 0 18 18"><circle cx="7" cy="7" r="5" fill="none" stroke="#fff" stroke-width="2.4"/><line x1="11" y1="11" x2="16" y2="16" stroke="#fff" stroke-width="2.8" stroke-linecap="round"/></svg>Find Homes</div>
    <div class="lang">Language: English<span class="sep">|</span><span>China</span><span class="sep">|</span><span>Vietnam</span></div>
    <div class="label" style="left:140px;top:64px">Type:</div>
    <div class="field" style="left:195px;top:56px;width:173px">Condo/Townhouse<i class="caret"></i></div>
    <div class="label" style="left:377px;top:64px">Price:</div>
    <div class="field" style="left:426px;top:56px;width:74px">$500k<i class="caret"></i></div>
    <div class="label" style="left:509px;top:64px">to:</div>
    <div class="field" style="left:536px;top:56px;width:75px">$1M<i class="caret"></i></div>
    <div class="label" style="left:622px;top:64px">Beds:</div>
    <div class="field" style="left:669px;top:56px;width:50px">3+<i class="caret"></i></div>
    <div class="label" style="left:732px;top:64px">Baths:</div>
    <div class="field" style="left:785px;top:56px;width:50px">3+<i class="caret"></i></div>
    <div class="nav" style="left:875px">Communities</div>
    <div class="nav" style="left:1000px">Locations</div>
    <div class="nav" style="left:1106px">Contact</div>
  </header>

  <section class="map" role="img" aria-label="Street map of the search area with property markers">
    <svg class="pin" style="left:120px;top:72px" width="20" height="26" viewBox="0 0 20 26"><path d="M10 25C4 16 1 13 1 9a9 9 0 0 1 18 0c0 4-3 7-9 16z" fill="var(--brand)"/><rect x="6" y="4" width="8" height="10" fill="#fff"/></svg>
    <svg class="pin" style="left:340px;top:72px" width="20" height="26" viewBox="0 0 20 26"><path d="M10 25C4 16 1 13 1 9a9 9 0 0 1 18 0c0 4-3 7-9 16z" fill="var(--brand)"/><rect x="6" y="4" width="8" height="10" fill="#fff"/></svg>
    <svg class="pin" style="left:527px;top:120px" width="20" height="26" viewBox="0 0 20 26"><path d="M10 25C4 16 1 13 1 9a9 9 0 0 1 18 0c0 4-3 7-9 16z" fill="var(--brand)"/><path d="M4 10l6-6 6 6v4H4z" fill="#fff"/></svg>
    <svg class="pin" style="left:703px;top:111px" width="20" height="26" viewBox="0 0 20 26"><path d="M10 25C4 16 1 13 1 9a9 9 0 0 1 18 0c0 4-3 7-9 16z" fill="var(--brand)"/><rect x="6" y="4" width="8" height="10" fill="#fff"/></svg>
    <svg class="pin" style="left:254px;top:153px" width="20" height="26" viewBox="0 0 20 26"><path d="M10 25C4 16 1 13 1 9a9 9 0 0 1 18 0c0 4-3 7-9 16z" fill="var(--brand)"/><path d="M4 10l6-6 6 6v4H4z" fill="#fff"/></svg>
    <svg class="pin" style="left:393px;top:174px" width="20" height="26" viewBox="0 0 20 26"><path d="M10 25C4 16 1 13 1 9a9 9 0 0 1 18 0c0 4-3 7-9 16z" fill="var(--brand)"/><path d="M4 10l6-6 6 6v4H4z" fill="#fff"/></svg>
    <svg class="pin" style="left:589px;top:218px" width="20" height="26" viewBox="0 0 20 26"><path d="M10 25C4 16 1 13 1 9a9 9 0 0 1 18 0c0 4-3 7-9 16z" fill="var(--brand)"/><rect x="6" y="4" width="8" height="10" fill="#fff"/></svg>
    <svg class="pin" style="left:790px;top:239px" width="20" height="26" viewBox="0 0 20 26"><path d="M10 25C4 16 1 13 1 9a9 9 0 0 1 18 0c0 4-3 7-9 16z" fill="var(--brand)"/><path d="M4 10l6-6 6 6v4H4z" fill="#fff"/></svg>
    <svg class="pin" style="left:204px;top:254px" width="20" height="26" viewBox="0 0 20 26"><path d="M10 25C4 16 1 13 1 9a9 9 0 0 1 18 0c0 4-3 7-9 16z" fill="var(--brand)"/><rect x="6" y="4" width="8" height="10" fill="#fff"/></svg>
    <svg class="pin" style="left:370px;top:313px" width="20" height="26" viewBox="0 0 20 26"><path d="M10 25C4 16 1 13 1 9a9 9 0 0 1 18 0c0 4-3 7-9 16z" fill="var(--brand)"/><rect x="6" y="4" width="8" height="10" fill="#fff"/></svg>
    <svg class="pin" style="left:538px;top:338px" width="20" height="26" viewBox="0 0 20 26"><path d="M10 25C4 16 1 13 1 9a9 9 0 0 1 18 0c0 4-3 7-9 16z" fill="var(--brand)"/><path d="M4 10l6-6 6 6v4H4z" fill="#fff"/></svg>
    <svg class="pin" style="left:745px;top:342px" width="20" height="26" viewBox="0 0 20 26"><path d="M10 25C4 16 1 13 1 9a9 9 0 0 1 18 0c0 4-3 7-9 16z" fill="var(--brand)"/><rect x="6" y="4" width="8" height="10" fill="#fff"/></svg>
    <svg class="pin" style="left:149px;top:372px" width="20" height="26" viewBox="0 0 20 26"><path d="M10 25C4 16 1 13 1 9a9 9 0 0 1 18 0c0 4-3 7-9 16z" fill="var(--brand)"/><path d="M4 10l6-6 6 6v4H4z" fill="#fff"/></svg>
    <svg class="pin" style="left:313px;top:381px" width="20" height="26" viewBox="0 0 20 26"><path d="M10 25C4 16 1 13 1 9a9 9 0 0 1 18 0c0 4-3 7-9 16z" fill="var(--brand)"/><rect x="6" y="4" width="8" height="10" fill="#fff"/></svg>
  </section>

  <section class="results">
    <div class="results-head">
      <span class="c1">Address</span><span class="c2">City</span><span class="c3">Price</span><span class="c4">Beds</span><span class="c5">Bats</span><span class="c6">Sq.Ft.</span><span class="c7">$/Sq.Ft.</span><span class="c8">Days</span>
    </div>
    <div class="rows">
      <div class="row"><span class="c1">1742 Vista Lomas Avenue</span><span class="c2">Rowland Heights</span><span class="c3">$1,200,000</span><span class="c4">4</span><span class="c5">2,5</span><span class="c6">1,814</span><span class="c7">$765</span><span class="c8">5</span></div>
      <div class="row"><span class="c1">1742 Vista Lomas Avenue</span><span class="c2">Rowland Heights</span><span class="c3">$1,200,000</span><span class="c4">4</span><span class="c5">2,5</span><span class="c6">1,814</span><span class="c7">$765</span><span class="c8">5</span></div>
      <div class="row"><span class="c1">1742 Vista Lomas Avenue</span><span class="c2">Rowland Heights</span><span class="c3">$1,200,000</span><span class="c4">4</span><span class="c5">2,5</span><span class="c6">1,814</span><span class="c7">$765</span><span class="c8">5</span></div>
      <div class="row"><span class="c1">1742 Vista Lomas Avenue</span><span class="c2">Rowland Heights</span><span class="c3">$1,200,000</span><span class="c4">4</span><span class="c5">2,5</span><span class="c6">1,814</span><span class="c7">$765</span><span class="c8">5</span></div>
      <div class="row"><span class="c1">1742 Vista Lomas Avenue</span><span class="c2">Rowland Heights</span><span class="c3">$1,200,000</span><span class="c4">4</span><span class="c5">2,5</span><span class="c6">1,814</span><span class="c7">$765</span><span class="c8">5</span></div>
      <div class="row"><span class="c1">1742 Vista Lomas Avenue</span><span class="c2">Rowland Heights</span><span class="c3">$1,200,000</span><span class="c4">4</span><span class="c5">2,5</span><span class="c6">1,814</span><span class="c7">$765</span><span class="c8">5</span></div>
      <div class="row"><span class="c1">1742 Vista Lomas Avenue</span><span class="c2">Rowland Heights</span><span class="c3">$1,200,000</span><span class="c4">4</span><span class="c5">2,5</span><span class="c6">1,814</span><span class="c7">$765</span><span class="c8">5</span></div>
      <div class="row"><span class="c1">1742 Vista Lomas Avenue</span><span class="c2">Rowland Heights</span><span class="c3">$1,200,000</span><span class="c4">4</span><span class="c5">2,5</span><span class="c6">1,814</span><span class="c7">$765</span><span class="c8">5</span></div>
    </div>
    <div class="table-scroll"><div class="thumb"></div></div>
  </section>

  <aside class="details">
    <h1 class="address" style="font-weight:400">1742 Vista Lomas Avenue<br>Rowland Heights</h1>
    <div class="photo" role="img" aria-label="Photo of the selected home: single-storey house with porch under a blue sky">
      <svg style="left:8px" width="10" height="14" viewBox="0 0 10 14"><path d="M8 1L2 7l6 6" fill="none" stroke="#fff" stroke-width="2.5"/></svg>
      <div class="count">1/32</div>
      <svg style="right:8px" width="10" height="14" viewBox="0 0 10 14"><path d="M2 1l6 6-6 6" fill="none" stroke="#fff" stroke-width="2.5"/></svg>
    </div>
    <div class="price">$2,388,000 Listing Price</div>
    <div class="specs">
      <svg width="18" height="12" viewBox="0 0 18 12"><path d="M1 1v10M1 8h16v3M4 5h13v3" fill="none" stroke="#aaa" stroke-width="1.5"/></svg>3
      <svg width="20" height="12" viewBox="0 0 20 12" style="margin-left:4px"><path d="M1 5h18c0 4-3 6-6 6H7C4 11 1 9 1 5zM3 5V2h3" fill="none" stroke="#aaa" stroke-width="1.5"/></svg>3
      <svg width="10" height="14" viewBox="0 0 10 14" style="margin-left:4px"><rect x="1.5" y="1" width="7" height="12" fill="none" stroke="#aaa" stroke-width="1.5"/><path d="M3 4h4M3 7h4M3 10h4" stroke="#aaa"/></svg>2014
    </div>
    <div class="facts">3,640 Sq.Ft ($656/Sq.Ft.)<br>9,889 Sq.Ft. Lot<br>25 Days on Market<br>#AR1234567890</div>
    <div class="btn" style="left:12px;width:136px">View Details</div>
    <div class="btn" style="left:154px;width:136px">Visit Home</div>
    <div class="courtesy">Courtesy of Harwell Pacific Realty</div>
    <div class="agent">
      <div class="agent-photo" role="img" aria-label="Portrait of the buyer's agent"></div>
      <div class="agent-info">Buyer's Agent<br><br><b>Mara Lindqvist</b><br>(626) 555-0148<br>mara@brightkey.example<br><br>BRE #4815162342</div>
    </div>
  </aside>

  <div class="page-scroll"><div class="thumb"></div></div>
</div>
</body>
</html>
```